Bref créative
Blue Maple Holdings, LLC
Business cards, stationary and envelopes, electronic stationary (Microsoft Word), email signature
Simple
Peter L. Ward
Managing Member
5180 Halvern Court, Suite A
Brookvale, KS 66999
pward@bmholdco.example
Phone, email, and name will change for the additional members of the company.
We also want an electronic email signature, and electronic stationary to be used with Microsoft word.
Stationary and envelopes should tie in the theme of the business cards for a uniform look.
Also looking for a Header only version of the stationary, as well as a full page version (header and footer used for design).
Logo used in a creative way.
Horizontal Black Background
Horizontal ALL Black
Horizontal White Background
Horizontal ALL White
Vertical Black Background
Vertical ALL Black
Vertical White Background
Vertical ALL White

```html
<!DOCTYPE html>
<html lang="en">
<head>
<meta charset="utf-8">
<title>Blue Maple Holdings – Business Card Presentation</title>
<link rel="stylesheet" href="https://fonts.googleapis.com/css2?family=Open+Sans:ital,wght@0,400;0,600;0,700;1,400&display=swap">
<style>
  :root {
    --board: #8a8a8a;
    --card-light: #ffffff;
    --card-dark: #2b2b2b;
    --brand-red: #c4202c;
    --ink-dark: #333333;
    --ink-light: #d6d6d6;
    --label: #f4f4f4;
  }
  * { margin: 0; padding: 0; box-sizing: border-box; }
  html, body { width: 1200px; height: 806px; overflow: hidden; }
  body {
    background: var(--board);
    font-family: "Open Sans", Arial, sans-serif;
    position: relative;
  }
  .card {
    position: absolute;
    width: 497px;
    height: 296px;
    box-shadow: 0 2px 6px rgba(0,0,0,.35);
  }
  .card--light { background: var(--card-light); color: var(--ink-dark); }
  .card--dark  { background: var(--card-dark);  color: var(--ink-light); }
  .pos-front-a { left: 72px;  top: 43px; }
  .pos-front-b { left: 638px; top: 43px; }
  .pos-back-a  { left: 72px;  top: 422px; }
  .pos-back-b  { left: 638px; top: 422px; }

  .brand {
    position: absolute;
    left: 0; right: 0;
    display: flex;
    align-items: center;
    justify-content: center;
    gap: 10px;
    color: var(--brand-red);
    font-weight: 700;
    letter-spacing: 2px;
    text-transform: uppercase;
    white-space: nowrap;
  }
  .brand__square {
    width: 28px; height: 28px;
    background: var(--brand-red);
    flex: none;
  }
  .card--front .brand { top: 84px; font-size: 24px; }
  .card--back .brand { top: 128px; font-size: 24px; }

  .member {
    position: absolute;
    left: 0; right: 0; top: 190px;
    text-align: center;
    font-size: 12px;
    white-space: nowrap;
  }
  .member__name { color: var(--brand-red); font-weight: 600; }
  .member__divider { margin: 0 4px; }
  .member__role { font-style: italic; }

  .contact {
    position: absolute;
    left: 0; right: 0; top: 230px;
    text-align: center;
    font-size: 9.5px;
    line-height: 14px;
    white-space: nowrap;
  }

  .label {
    position: absolute;
    width: 497px;
    text-align: center;
    color: var(--label);
    font-size: 20px;
    letter-spacing: 3px;
    font-variant: small-caps;
    white-space: nowrap;
  }
  .label--front-a { left: 72px;  top: 346px; }
  .label--front-b { left: 638px; top: 346px; }
  .label--back-a  { left: 72px;  top: 740px; }
  .label--back-b  { left: 638px; top: 740px; }
</style>
</head>
<body>

<section class="card card--light card--front pos-front-a">
  <div class="brand"><span class="brand__square"></span><span>Blue Maple Holdings</span></div>
  <p class="member"><span class="member__name">Peter L. Ward</span><span class="member__divider">|</span><span class="member__role">Managing Member</span></p>
  <p class="contact">5180 Halvern Court, Suite A Brookvale, KS 66999 | E: pward@bmholdco.example<br>P: (555) 014-2210 | C: (555) 014-2210 | F: (555) 014-2288</p>
</section>

<section class="card card--dark card--front pos-front-b">
  <div class="brand"><span class="brand__square"></span><span>Blue Maple Holdings</span></div>
  <p class="member"><span class="member__name">Peter L. Ward</span><span class="member__divider">|</span><span class="member__role">Managing Member</span></p>
  <p class="contact">5180 Halvern Court, Suite A Brookvale, KS 66999 | E: pward@bmholdco.example<br>P: (555) 014-2210 | C: (555) 014-2210 | F: (555) 014-2288</p>
</section>

<p class="label label--front-a">Business Card Front A</p>
<p class="label label--front-b">Business Card Front B</p>

<section class="card card--light card--back pos-back-a">
  <div class="brand"><span class="brand__square"></span><span>Blue Maple Holdings</span></div>
</section>

<section class="card card--dark card--back pos-back-b">
  <div class="brand"><span class="brand__square"></span><span>Blue Maple Holdings</span></div>
</section>

<p class="label label--back-a">Business Card Back A</p>
<p class="label label--back-b">Business Card Back B</p>

</body>
</html>
```